Listing Presentation for The Harbin Circle of Pellworth Realty

We need a unique listing presentation for homeowners interested in selling their home. The presentation should communicate our knowledge of the selling process, the market and our strengths as a real estate team. A cohesive look that conveys our belief of putting our clients and their families first.

Target Market(s)

Homeowners interested in selling their home

Industry/Entity Type

Real Estate

Font styles to use
Sans Serif

Colors
0255a3
9bcb3c

Requirements
Must have
• -color match those of our logo: #11214a #98EO61
• -template so we can add additional pages as needed

```html
<!DOCTYPE html>
<html lang="en">
<head>
<meta charset="utf-8">
<title>The Harbin Circle – Listing Presentation</title>
<link rel="stylesheet" href="https://fonts.googleapis.com/css2?family=Montserrat:wght@400;500;600;700;800&display=swap">
<style>
  :root{
    --navy:#1b2a5e;
    --green:#9bcb3c;
    --white:#ffffff;
    --page:#e6e7e9;
    --ink:#1b2a5e;
  }
  *{margin:0;padding:0;box-sizing:border-box}
  html,body{width:1200px;height:1200px;overflow:hidden;background:var(--page);font-family:"Montserrat",sans-serif}
  .deck{position:relative;width:1200px;height:1200px}
  .slide{position:absolute;width:491px;height:347px;overflow:hidden;background:var(--white)}
  .col-a{left:85px}.col-b{left:625px}
  .row-1{top:42px}.row-2{top:426px}.row-3{top:810px}
  .photo{position:absolute}
  .shapes{position:absolute;left:0;top:0;width:491px;height:347px}
  .abs{position:absolute}

  /* cover */
  .brand{left:25px;top:22px;display:flex;align-items:center;gap:7px;color:var(--navy)}
  .brand-mark{width:26px;height:26px;background:var(--navy)}
  .brand-name{font-weight:700;font-size:12px;line-height:1.1}
  .brand-line{font-size:5.5px;font-weight:600;letter-spacing:.3px}
  .brand-sub{font-size:5.5px;font-weight:500}
  .cover-title{right:18px;top:302px;text-align:right;color:var(--white)}
  .cover-title h1{font-size:18px;font-weight:700;letter-spacing:.2px}
  .cover-title p{font-size:11px;font-weight:400}

  /* headings */
  .big{font-weight:800;line-height:.9;letter-spacing:-1px}
  .sub{font-weight:700;line-height:1}
  .body{font-size:8.5px;line-height:1.42;font-weight:500}

  .purpose{left:325px;top:68px;width:145px;color:var(--navy)}
  .purpose .big{font-size:56px}
  .purpose .sub{font-size:26px}
  .purpose .mission{font-size:16px;font-weight:600;letter-spacing:4px;margin:2px 0 12px}
  .purpose .body{text-align:justify}

  .about-title{left:36px;top:28px;color:var(--navy)}
  .about-title .sub{font-size:22px}
  .about-title .big{font-size:54px}
  .about-tag{left:138px;top:30px;color:var(--navy);font-size:9.5px;line-height:1.45;font-weight:500}

  .approach{left:31px;top:40px;width:150px;color:var(--white)}
  .approach .big{font-size:56px}
  .approach .sub{font-size:23px;margin-bottom:10px}
  .approach .body{text-align:justify;opacity:.9}
  .pillar{top:187px;width:140px;height:68px;background:var(--navy);border-radius:4px;padding:5px 9px;color:var(--white)}
  .pillar h3{font-size:10.5px;font-weight:700;margin-bottom:4px}
  .pillar p{font-size:6px;line-height:1.5;opacity:.85}

  .believe{left:134px;top:132px;color:var(--white);text-align:right}
  .believe .big{font-size:64px}
  .believe .sub{font-size:26px}
  .believe-note{left:263px;top:135px;width:100px;height:80px;border:1px solid rgba(255,255,255,.6);border-left-width:1px;padding:4px 0 0 10px;color:var(--white);font-size:9px;line-height:1.4;font-weight:400}
  .believe-note::after{content:"";position:absolute;left:8px;right:8px;top:-1px;bottom:-1px;background:transparent;border-top:1px solid rgba(0,0,0,0);}

  .history-head{left:28px;top:21px;width:380px;color:var(--navy)}
  .history-head h2{font-size:13px;font-weight:700;margin-bottom:5px}
  .history-head p{font-size:8.4px;line-height:1.4;font-weight:500}
  .history-title{right:33px;top:236px;color:var(--white);text-align:right}
  .history-title .big{font-size:56px}
  .history-title .sub{font-size:27px}
</style>
</head>
<body>
<main class="deck">

  <!-- Cover -->
  <section class="slide col-a row-1">
    <div class="abs brand">
      <span class="brand-mark"></span>
      <div>
        <div class="brand-name">THE HARBIN CIRCLE</div>
        <div class="brand-line">BRING YOUR DREAM HOME</div>
        <div class="brand-sub">The Harbin Circle of Pellworth Realty</div>
      </div>
    </div>
    <div class="photo" role="img" aria-label="Modern bedroom interior with glass wall opening onto a wooded hillside" style="left:0;top:76px;width:491px;height:271px;background:linear-gradient(90deg,#b9a58a 0%,#d9d2c4 35%,#8e8c7c 60%,#5f8a4a 80%,#7fa55a 100%)"></div>
    <svg class="shapes" viewBox="0 0 491 347" aria-hidden="true">
      <polygon points="0,300 491,254 491,347 0,347" fill="var(--green)" opacity=".92"/>
      <polygon points="0,188 0,347 140,347" fill="var(--navy)"/>
    </svg>
    <div class="abs cover-title">
      <h1>BRING YOUR DREAM HOME</h1>
      <p>The Harbin Circle of Pellworth Realty</p>
    </div>
  </section>

  <!-- Purpose -->
  <section class="slide col-b row-1">
    <div class="photo" role="img" aria-label="Smiling family of four standing in front of a white house" style="left:0;top:0;width:491px;height:347px;background:linear-gradient(90deg,#a9c7de 0%,#d8c2a8 30%,#e6d3bd 55%,#f2f1ee 75%,#fbfbfb 100%)"></div>
    <svg class="shapes" viewBox="0 0 491 347" aria-hidden="true">
      <polygon points="0,186 0,347 145,347" fill="var(--navy)"/>
    </svg>
    <div class="abs purpose">
      <div class="big">OUR</div>
      <div class="sub">PURPOSE</div>
      <div class="mission">(mission)</div>
      <p class="body">Our purpose is to listen and to get you HOME. The Real Estate market is complex and moves fast. We understand the process, we've chosen partners based on results and integrity, and we want empower YOU to make the choises that are the best for your family.</p>
    </div>
  </section>

  <!-- About -->
  <section class="slide col-a row-2">
    <div class="photo" role="img" aria-label="Team of five cheering with raised arms in a bright office" style="left:0;top:95px;width:491px;height:252px;background:linear-gradient(180deg,#f4f6f8 0%,#d9dde2 45%,#6f6f78 75%,#3c4250 100%)"></div>
    <svg class="shapes" viewBox="0 0 491 347" aria-hidden="true">
      <polygon points="0,300 491,250 491,347 0,347" fill="var(--green)" opacity=".9"/>
      <polygon points="0,185 0,347 140,347" fill="var(--navy)"/>
    </svg>
    <div class="abs about-title">
      <div class="sub">ABOUT</div>
      <div class="big">US</div>
    </div>
    <p class="abs about-tag">We celebrate milestones. We are grateful.<br>We think time is valuable and we dream BIG!</p>
  </section>

  <!-- Approach -->
  <section class="slide col-b row-2">
    <div class="photo" role="img" aria-label="Hands reviewing a document beside a small model house, blue tinted" style="left:0;top:0;width:491px;height:347px;background:linear-gradient(135deg,#4a63a6 0%,#7d93c9 40%,#b7c4e3 70%,#e4e9f4 100%)"></div>
    <svg class="shapes" viewBox="0 0 491 347" aria-hidden="true">
      <polygon points="491,0 491,347 145,347" fill="#ffffff" opacity=".35"/>
      <polygon points="0,255 0,347 145,347" fill="var(--navy)"/>
    </svg>
    <div class="abs approach">
      <div class="big">OUR</div>
      <div class="sub">APPROACH</div>
      <p class="body">We understand we are not just buying and selling houses but BRINGING DREAMS HOME; therefore, our approcah starts with you.</p>
    </div>
    <div class="abs pillar" style="left:28px">
      <h3>PEOPLE FIRST</h3>
      <p>Our main goal is protect YOUR best interest. We want you to know you have someone fighting for you when you're not in the room.</p>
    </div>
    <div class="abs pillar" style="left:176px">
      <h3>PROCESS</h3>
      <p>We are committed to transparency and open communication so you can make informed decisions every step of the way.</p>
    </div>
    <div class="abs pillar" style="left:324px">
      <h3>PEOPLE FIRST</h3>
      <p>Each real estate purchase is unique. We guide the process to completion and BRING YOUR DREAM. HOME</p>
    </div>
  </section>

  <!-- Believe -->
  <section class="slide col-a row-3">
    <div class="photo" role="img" aria-label="Stone family house at dusk with a curving driveway, purple tinted" style="left:0;top:0;width:491px;height:347px;background:linear-gradient(180deg,#4a4f86 0%,#5e5a8a 40%,#4d5a82 65%,#3f4a78 100%)"></div>
    <div class="abs believe">
      <div class="big">WE</div>
      <div class="sub">BELIEVE</div>
    </div>
    <p class="abs believe-note">We believe you deserve a champion in the complex process of Real Estate.</p>
  </section>

  <!-- History -->
  <section class="slide col-b row-3">
    <div class="abs history-head">
      <h2>Committed to People and Service</h2>
      <p>Founder and Alder County Fire Captain, Daniel Ostrander, is known for his inclusive and composed leadership style, which was crafted and refined through his 18 years of service in Fire and Rescue. the value-system of "people first" that built his career serves as the same foundation for The Harbin Circle today.</p>
    </div>
    <div class="photo" role="img" aria-label="Father embracing two children at the front door of a home" style="left:0;top:101px;width:491px;height:246px;background:linear-gradient(90deg,#c9a784 0%,#e8ddd0 35%,#9a8f8a 55%,#e9ecec 80%,#f6f7f5 100%)"></div>
    <svg class="shapes" viewBox="0 0 491 347" aria-hidden="true">
      <polygon points="491,0 491,347 145,347" fill="var(--green)" opacity=".92"/>
      <polygon points="0,186 0,347 145,347" fill="var(--navy)"/>
    </svg>
    <div class="abs history-title">
      <div class="big">OUR</div>
      <div class="sub">HISTORY</div>
    </div>
  </section>

</main>
</body>
</html>
```